WP website design (Whitlock)

We need a wordpress design for an established auction and real estate company based in Daswon Creek, Canada. The winning design will incorporate a professional color scheme with company logo in a clean layout with specified widgets. The design needs to consider that this will be developed on a responsive theme. Colors will complement logo - red, black and gray.

Industry/Entity Type

Real Estate

Font styles to use
Sans Serif

Requirements
Must have
• Must Have:
the main logo is provided and the 'horse' logo shouldbe incorporated into the hearder or sidebar (either left or right)as well. Contact info should be placed in the header, and footer too: (250) 555-0143
(250) 555-0178
(250) 555-0192
rvm@zorquil.bc.ca

- Navigation:
1) Home 2) Auctions 3) Online Auctions 4) About Us 5) Contact Us

Home Page will have following:
"Family owned and operated with a family guarantee.
Located in Dawson Creek, B.C. Canada

Competitive Rates Bonded & Licensed Livestock Dealers & Auctioneers
All Types of Auction Sales in B.C. & Alberta

Farm, Machinery
Equipment Sales
Household & Estate Sales
Livestock Marketing Consultants
Field Cattle Sales
Livestock Pedigree Sales
Horse Sales Appraisals"

Homepage will have auctions - as at http://brindlevexsales.com/upcoming-auctions/.

Footer will have smaller company logo, credit card logo, and attached association logos and this contact info:
.(620) 555-0117: OFFICE
(620) 555-0164: FAX
hgrup@vxq.com: email
Address: 718 N. Birch Ave., Johnson KS
Mailing Address: PO Box 839, Quillan, KS

Widgets:
1) email sign up 2) News blog widget 3) testimonial blog widget 4) featured auctions widget 5) the 'Gold Peg' logo which is included
Nice to have
• Nice to Have:
- demonstrate the drop-down menu styling, e.g. under Auctions
- Upcoming Auctions
- Past Auctions

```html
<!DOCTYPE html>
<html lang="en">
<head>
<meta charset="utf-8">
<title>Whitlock Auction Sales</title>
<link href="https://fonts.googleapis.com/css2?family=Arvo:wght@400;700&family=Open+Sans:wght@400;600;700&display=swap" rel="stylesheet">
<style>
:root{
  --red:#c0281f;
  --red-dark:#8f1a14;
  --ink:#222;
  --charcoal:#2b2b2b;
  --text:#555;
  --muted:#888;
  --line:#e1e1e1;
  --page:#f0f0f0;
  --white:#fff;
}
*{box-sizing:border-box;margin:0;padding:0}
html,body{width:1200px;height:2232px;overflow:hidden}
body{font-family:"Open Sans",Arial,sans-serif;color:var(--text);background:var(--white);font-size:13px;position:relative}
.wrap{width:1000px;margin:0 auto;position:relative}

/* header */
.site-header{height:112px}
.site-header .wrap{height:112px;display:flex;align-items:center;justify-content:space-between}
.brand{display:flex;align-items:center;gap:12px}
.brand-mark{width:40px;height:40px;background:var(--charcoal)}
.brand-name{font-family:"Arvo",Georgia,serif;font-weight:700;font-size:17px;color:var(--charcoal);line-height:1.15;width:170px}
.header-right{display:flex;align-items:center;gap:40px}
.partner{display:flex;align-items:center;gap:8px;border:1px solid var(--line);padding:10px 16px}
.partner-square{width:18px;height:18px;background:var(--red)}
.partner-name{font-family:"Arvo",Georgia,serif;font-weight:700;font-size:18px;color:var(--charcoal)}
.header-contact{list-style:none;font-size:12px;color:var(--text);line-height:18px}
.header-contact li{display:flex;align-items:center;gap:6px}
.header-contact svg{width:11px;height:11px;fill:var(--red)}

/* nav */
.main-nav{background:var(--red);height:38px;position:relative;z-index:2}
.main-nav ul{list-style:none;display:flex}
.main-nav > .wrap > ul > li{position:relative}
.main-nav a{display:block;color:var(--white);text-decoration:none;font-size:13px;line-height:38px;padding:0 22px}
.main-nav li.active > a{background:var(--red-dark)}
.dropdown{position:absolute;top:38px;left:0;width:170px;background:var(--red-dark);flex-direction:column;display:flex}
.dropdown a{line-height:30px;font-size:12px;padding:0 16px;border-top:1px solid rgba(255,255,255,.15)}

/* hero */
.hero{height:410px;background:linear-gradient(180deg,#9cb6cf 0%,#c9d6df 45%,#9b8f82 70%,#4d8fb0 100%);position:relative}
.hero-box{position:absolute;left:100px;top:98px;width:480px;background:rgba(25,25,25,.82);padding:26px 28px}
.hero-box h1{font-family:"Arvo",Georgia,serif;font-weight:400;color:var(--white);font-size:31px;line-height:40px}
.hero-location{margin-top:16px;padding-top:14px;border-top:1px solid rgba(255,255,255,.2);color:#ddd;font-size:13px;letter-spacing:1px;display:flex;gap:8px;align-items:center}
.hero-location svg{width:12px;height:16px;fill:var(--white)}

/* band */
.promise-band{background:var(--charcoal);height:76px}
.promise-band .wrap{height:76px;display:flex;justify-content:center;align-items:center;gap:70px}
.promise{display:flex;align-items:center;gap:12px;color:var(--white);font-family:"Arvo",Georgia,serif;font-size:22px}
.promise svg{width:24px;height:24px;fill:var(--white)}

/* services */
.services{height:224px;padding-top:30px;text-align:center}
.services h2{font-family:"Arvo",Georgia,serif;color:var(--red);font-size:19px;font-weight:400;margin-bottom:20px}
.service-cols{display:flex;justify-content:center;gap:90px;text-align:left}
.service-cols ul{list-style:none;font-size:13px;color:var(--ink);line-height:24px}
.service-cols li::before{content:"";display:inline-block;width:6px;height:6px;background:var(--red);border-radius:50%;margin-right:10px;vertical-align:middle}

/* main */
.main{background:var(--page);height:1190px;padding-top:18px}
.main .wrap{display:flex;justify-content:space-between}
.auction-list{width:660px}
.auction-card{background:var(--white);height:220px;margin-bottom:28px;display:flex;padding:18px;border:1px solid var(--line)}
.auction-media{width:200px;display:flex;flex-direction:column;gap:8px}
.auction-photo{height:148px;background:linear-gradient(180deg,#b7c7d4,#8d8172 65%,#6f7d56)}
.btn-red{background:var(--red);color:var(--white);font-size:11px;font-weight:700;text-align:center;line-height:26px;text-transform:uppercase}
.auction-body{flex:1;padding-left:22px}
.auction-body h3{font-family:"Arvo",Georgia,serif;font-weight:400;color:var(--red);font-size:20px}
.auction-desc{font-size:11px;color:var(--muted);line-height:16px;margin:6px 0 10px}
.auction-date{font-size:11px;color:var(--text);display:flex;align-items:center;gap:6px}
.auction-date svg{width:11px;height:11px;fill:var(--muted)}
.auction-tags{display:flex;gap:10px;margin:12px 0}
.tag{flex:1;font-size:10px;font-weight:700;text-align:center;line-height:26px;border:1px solid var(--line);text-transform:uppercase}
.tag.dark{color:var(--ink)}
.tag.live{color:var(--red)}
.auction-times{font-size:11px;line-height:18px;color:var(--text)}

.pagination{display:flex;justify-content:center;gap:4px;margin-top:40px}
.pagination span{width:24px;height:24px;line-height:24px;text-align:center;font-size:11px;background:var(--white);border:1px solid var(--line)}
.pagination span.on{background:var(--red);color:var(--white);border-color:var(--red)}

.sidebar{width:300px}
.widget{margin-bottom:20px}
.featured{background:var(--red);padding:14px;color:var(--white);height:232px}
.featured h4{font-family:"Arvo",Georgia,serif;font-weight:400;font-size:16px;margin-bottom:10px}
.featured-photo{height:100px;background:linear-gradient(180deg,#a9bfd0,#8c7e6d 70%,#6f7b55)}
.featured-dates{font-size:11px;font-weight:700;line-height:16px;margin:10px 0;text-align:center}
.btn-dark{background:var(--charcoal);color:var(--white);font-size:11px;font-weight:700;text-align:center;line-height:28px;text-transform:uppercase}
.notify{background:var(--white);border:1px solid var(--line);padding:18px;height:202px}
.widget-title{font-family:"Arvo",Georgia,serif;font-weight:400;font-size:17px;color:var(--ink);margin-bottom:10px}
.notify p{font-size:11px;color:var(--muted);line-height:16px;margin-bottom:12px}
.field{height:32px;border:1px solid var(--line);font-size:11px;color:#aaa;line-height:30px;padding:0 10px;margin-bottom:10px}
.notify .btn-red{line-height:32px}
.blog-item{display:flex;gap:12px;margin-bottom:16px}
.blog-thumb{width:52px;height:52px;border-radius:50%;background:#b9b1a5;flex:none}
.blog-item p{font-size:11px;color:var(--text);line-height:16px}
.blog-item small{display:block;font-size:10px;color:var(--muted);margin-top:4px}
.client{display:flex;align-items:center;gap:12px;margin-bottom:12px}
.client-avatar{width:52px;height:52px;border-radius:50%;background:#9a9a9a}
.client-name{font-weight:600;color:var(--ink);font-size:13px}
.quote{background:#8f8f8f;color:var(--white);font-size:12px;line-height:18px;padding:16px 18px;font-style:italic}

/* footer */
.site-footer{height:150px;background:var(--white);border-top:1px solid var(--line)}
.site-footer .wrap{display:flex;justify-content:space-between;padding-top:20px}
.footer-brand{display:flex;align-items:center;gap:10px;width:220px;align-self:center}
.footer-brand .brand-mark{width:32px;height:32px}
.footer-brand .brand-name{font-size:14px;width:140px}
.footer-col h5{font-family:"Arvo",Georgia,serif;font-weight:400;font-size:13px;color:var(--ink);margin-bottom:6px}
.footer-col ul{list-style:none;font-size:10px;color:var(--muted);line-height:16px}
.footer-col li{display:flex;gap:5px;align-items:center}
.footer-col svg{width:9px;height:9px;fill:var(--red)}
.cards,.social{display:flex;gap:6px;margin-bottom:8px}
.cards span{width:32px;height:20px;background:#d6d6d6;border-radius:2px}
.social span{width:22px;height:22px;background:var(--charcoal)}
.bottom-bar{height:32px;background:var(--charcoal)}
.bottom-bar .wrap{display:flex;justify-content:space-between;line-height:32px;font-size:10px;color:#bbb}
</style>
</head>
<body>

<header class="site-header">
  <div class="wrap">
    <div class="brand">
      <span class="brand-mark"></span>
      <span class="brand-name">Whitlock Auction Sales Ltd.</span>
    </div>
    <div class="header-right">
      <div class="partner"><span class="partner-square"></span><span class="partner-name">Gold Peg</span></div>
      <ul class="header-contact">
        <li><svg viewBox="0 0 24 24"><path d="M6.6 10.8a15 15 0 006.6 6.6l2.2-2.2c.3-.3.7-.4 1-.2 1.1.4 2.3.6 3.6.6.6 0 1 .4 1 1V20c0 .6-.4 1-1 1A17 17 0 013 4c0-.6.4-1 1-1h3.5c.6 0 1 .4 1 1 0 1.3.2 2.5.6 3.6.1.3 0 .7-.2 1z"/></svg>(250) 555-0143</li>
        <li><svg viewBox="0 0 24 24"><path d="M6.6 10.8a15 15 0 006.6 6.6l2.2-2.2c.3-.3.7-.4 1-.2 1.1.4 2.3.6 3.6.6.6 0 1 .4 1 1V20c0 .6-.4 1-1 1A17 17 0 013 4c0-.6.4-1 1-1h3.5c.6 0 1 .4 1 1 0 1.3.2 2.5.6 3.6.1.3 0 .7-.2 1z"/></svg>(250) 555-0178</li>
        <li><svg viewBox="0 0 24 24"><path d="M6.6 10.8a15 15 0 006.6 6.6l2.2-2.2c.3-.3.7-.4 1-.2 1.1.4 2.3.6 3.6.6.6 0 1 .4 1 1V20c0 .6-.4 1-1 1A17 17 0 013 4c0-.6.4-1 1-1h3.5c.6 0 1 .4 1 1 0 1.3.2 2.5.6 3.6.1.3 0 .7-.2 1z"/></svg>(250) 555-0192</li>
        <li><svg viewBox="0 0 24 24"><path d="M2 5h20v14H2zm2 2v.5l8 5 8-5V7z"/></svg>rvm@zorquil.bc.ca</li>
      </ul>
    </div>
  </div>
</header>

<nav class="main-nav">
  <div class="wrap">
    <ul>
      <li><a href="#">Home</a></li>
      <li class="active"><a href="#">Auctions</a>
        <ul class="dropdown">
          <li><a href="#">Upcoming Auctions</a></li>
          <li><a href="#">Past Auctions</a></li>
        </ul>
      </li>
      <li><a href="#">Online Auctions</a></li>
      <li><a href="#">About</a></li>
      <li><a href="#">Contact</a></li>
    </ul>
  </div>
</nav>

<section class="hero" role="img" aria-label="Photo of a large family home with a pool under a blue sky">
  <div class="hero-box">
    <h1>Family owned and operated with a family guarantee.</h1>
    <p class="hero-location"><svg viewBox="0 0 12 16"><path d="M6 0a6 6 0 00-6 6c0 4.5 6 10 6 10s6-5.5 6-10a6 6 0 00-6-6zm0 8.5A2.5 2.5 0 116 3.5a2.5 2.5 0 010 5z"/></svg>LOCATED IN DAWSON CREEK, B.C. CANADA</p>
  </div>
</section>

<section class="promise-band">
  <div class="wrap">
    <div class="promise"><svg viewBox="0 0 24 24"><path d="M9 16.2l-4.2-4.2L3.4 13.4 9 19 21 7l-1.4-1.4z"/></svg>Competitive Rates Bonded</div>
    <div class="promise"><svg viewBox="0 0 24 24"><path d="M9 16.2l-4.2-4.2L3.4 13.4 9 19 21 7l-1.4-1.4z"/></svg>Licensed Livestock Dealers &amp; Auctioneers</div>
  </div>
</section>

<section class="services">
  <div class="wrap">
    <h2>All Types of Auction Sales in B.C. &amp; Alberta</h2>
    <div class="service-cols">
      <ul><li>Farm, Machinery</li><li>Equipment Sales</li></ul>
      <ul><li>Household &amp; Estate Sales</li><li>Livestock Marketing Consultants</li><li>Field Cattle Sales</li></ul>
      <ul><li>Livestock Pedigree Sales</li><li>Horse Sales Appraisals</li></ul>
    </div>
  </div>
</section>

<main class="main">
  <div class="wrap">
    <div class="auction-list">
      <article class="auction-card">
        <div class="auction-media"><div class="auction-photo" role="img" aria-label="Photo of the auction property"></div><div class="btn-red">View Online Bidding</div></div>
        <div class="auction-body">
          <h3>Test Auction</h3>
          <p class="auction-desc">Annual spring consignment sale featuring farm machinery, livestock equipment and household items.</p>
          <p class="auction-date"><svg viewBox="0 0 12 12"><path d="M1 2h10v9H1zm1 3v5h8V5z"/></svg>Fri Mar 28th | Dawson Creek, B.C.</p>
          <div class="auction-tags"><span class="tag dark">Online Bidding Only</span><span class="tag live">Live Site Auction</span></div>
          <p class="auction-times">Begins : Tuesday, March 04, 2014 at 10:00 AM PST<br>Ends : Tuesday, March 11, 2014 at 12:00 PM PST</p>
        </div>
      </article>
      <article class="auction-card">
        <div class="auction-media"><div class="auction-photo" role="img" aria-label="Photo of the auction property"></div><div class="btn-red">View Online Bidding</div></div>
        <div class="auction-body">
          <h3>Test Auction</h3>
          <p class="auction-desc">Annual spring consignment sale featuring farm machinery, livestock equipment and household items.</p>
          <p class="auction-date"><svg viewBox="0 0 12 12"><path d="M1 2h10v9H1zm1 3v5h8V5z"/></svg>Fri Mar 28th | Dawson Creek, B.C.</p>
          <div class="auction-tags"><span class="tag dark">Online Bidding Only</span><span class="tag live">Live Site Auction</span></div>
          <p class="auction-times">Begins : Tuesday, March 04, 2014 at 10:00 AM PST<br>Ends : Tuesday, March 11, 2014 at 12:00 PM PST</p>
        </div>
      </article>
      <article class="auction-card">
        <div class="auction-media"><div class="auction-photo" role="img" aria-label="Photo of the auction property"></div><div class="btn-red">View Online Bidding</div></div>
        <div class="auction-body">
          <h3>Test Auction</h3>
          <p class="auction-desc">Annual spring consignment sale featuring farm machinery, livestock equipment and household items.</p>
          <p class="auction-date"><svg viewBox="0 0 12 12"><path d="M1 2h10v9H1zm1 3v5h8V5z"/></svg>Fri Mar 28th | Dawson Creek, B.C.</p>
          <div class="auction-tags"><span class="tag dark">Online Bidding Only</span><span class="tag live">Live Site Auction</span></div>
          <p class="auction-times">Begins : Tuesday, March 04, 2014 at 10:00 AM PST<br>Ends : Tuesday, March 11, 2014 at 12:00 PM PST</p>
        </div>
      </article>
      <article class="auction-card">
        <div class="auction-media"><div class="auction-photo" role="img" aria-label="Photo of the auction property"></div><div class="btn-red">View Online Bidding</div></div>
        <div class="auction-body">
          <h3>Test Auction</h3>
          <p class="auction-desc">Annual spring consignment sale featuring farm machinery, livestock equipment and household items.</p>
          <p class="auction-date"><svg viewBox="0 0 12 12"><path d="M1 2h10v9H1zm1 3v5h8V5z"/></svg>Fri Mar 28th | Dawson Creek, B.C.</p>
          <div class="auction-tags"><span class="tag dark">Online Bidding Only</span><span class="tag live">Live Site Auction</span></div>
          <p class="auction-times">Begins : Tuesday, March 04, 2014 at 10:00 AM PST<br>Ends : Tuesday, March 11, 2014 at 12:00 PM PST</p>
        </div>
      </article>
      <div class="pagination"><span>&lsaquo;</span><span class="on">1</span><span>2</span><span>3</span><span>4</span><span>&rsaquo;</span></div>
    </div>

    <aside class="sidebar">
      <div class="widget featured">
        <h4>Featured Auction</h4>
        <div class="featured-photo" role="img" aria-label="Photo of the featured auction home"></div>
        <p class="featured-dates">05/28/17 at 2:00 PM MST<br>05/28/17 at 4:00 PM MST</p>
        <div class="btn-dark">View Details</div>
      </div>
      <div class="widget notify">
        <h4 class="widget-title">Notify me of upcoming auctions</h4>
        <p>Sign up to our newsletter to get notified of upcoming auctions near you.</p>
        <div class="field">Your email address</div>
        <div class="btn-red">Subscribe Now</div>
      </div>
      <div class="widget">
        <h4 class="widget-title">Latest Blog</h4>
        <div class="blog-item"><div class="blog-thumb" role="img" aria-label="Blog post thumbnail"></div><p>Spring cattle market outlook for northern B.C. producers<small>March 12, 2014</small></p></div>
        <div class="blog-item"><div class="blog-thumb" role="img" aria-label="Blog post thumbnail"></div><p>How to prepare your equipment before consignment day<small>March 05, 2014</small></p></div>
        <div class="blog-item"><div class="blog-thumb" role="img" aria-label="Blog post thumbnail"></div><p>Estate sale tips for families settling a farm<small>February 26, 2014</small></p></div>
      </div>
      <div class="widget">
        <h4 class="widget-title">Client Testimonial</h4>
        <div class="client"><div class="client-avatar" role="img" aria-label="Client portrait"></div><span class="client-name">Reed Calloway</span></div>
        <p class="quote">Fair prices, honest people and a sale day that ran like clockwork. We will be back.</p>
      </div>
    </aside>
  </div>
</main>

<footer class="site-footer">
  <div class="wrap">
    <div class="footer-brand"><span class="brand-mark"></span><span class="brand-name">Whitlock Auction Sales Ltd.</span></div>
    <div class="footer-col">
      <h5>Navigation</h5>
      <ul><li>Home</li><li>Auctions</li><li>Online Auctions</li><li>About Us</li><li>Contact Us</li></ul>
    </div>
    <div class="footer-col">
      <h5>Contact Us</h5>
      <ul>
        <li><svg viewBox="0 0 24 24"><path d="M6.6 10.8a15 15 0 006.6 6.6l2.2-2.2c.3-.3.7-.4 1-.2 1.1.4 2.3.6 3.6.6.6 0 1 .4 1 1V20c0 .6-.4 1-1 1A17 17 0 013 4c0-.6.4-1 1-1h3.5c.6 0 1 .4 1 1 0 1.3.2 2.5.6 3.6.1.3 0 .7-.2 1z"/></svg>(620) 555-0117 : Office</li>
        <li><svg viewBox="0 0 24 24"><path d="M4 4h16v16H4z"/></svg>(620) 555-0164 : Fax</li>
        <li><svg viewBox="0 0 24 24"><path d="M2 5h20v14H2zm2 2v.5l8 5 8-5V7z"/></svg>hgrup@vxq.com</li>
        <li><svg viewBox="0 0 12 16"><path d="M6 0a6 6 0 00-6 6c0 4.5 6 10 6 10s6-5.5 6-10a6 6 0 00-6-6z"/></svg>718 N. Birch Ave., Quillan KS</li>
        <li><svg viewBox="0 0 12 16"><path d="M6 0a6 6 0 00-6 6c0 4.5 6 10 6 10s6-5.5 6-10a6 6 0 00-6-6z"/></svg>PO Box 839, Quillan, KS</li>
      </ul>
    </div>
    <div class="footer-col">
      <h5>We Accept</h5>
      <div class="cards"><span></span><span></span><span></span><span></span></div>
      <div class="social"><span></span><span></span><span></span></div>
    </div>
  </div>
</footer>
<div class="bottom-bar">
  <div class="wrap"><span>Copyright 2014 Whitlock Auction Sales Ltd. &middot; All Rights Reserved</span><span>Site Map &nbsp;|&nbsp; Privacy Policy</span></div>
</div>

</body>
</html>
```